■依頼の目的/概要
ビジネス本の表紙デザインをお願いします。

■本の内容
・起業初期の起業家、または副業で月収入10万円UPしたい方向けの、
77のWEBのアドバイス(テクニック)をまとめた本です。

■デザイン要望
どちらかというと、30~50代女性起業家向けです。
女性のイラストが入ると嬉しいです。

その他何かご不明な点がございましたら、お気軽にご質問下さい。
よろしくお願いいたします。

■プレセントの記載をお願いします。
①何が足りないかすぐ分かる!
WEBチェックシート

②1年で1万人フォロワーを達成した
Plumoraフォロワー増やしのコツ

③最短で成功へ向かう無料コンサル

女性らしい優しい雰囲気で、誰からも愛されるデザインと感じました。

この度はご応募頂き、誠にありがとうございました!

どのデザインも素敵で、本当に迷いました。
修正していただいた方には、親切に対応して頂き心より感謝しております。

皆様の益々のご活躍を祈念しております。
今回は本当に有難うございました。

```html
<!DOCTYPE html>
<html lang="ja">
<head>
<meta charset="UTF-8">
<title>知っておくべきWEBテクニック77のポイント 逆引き辞典</title>
<link rel="stylesheet" href="https://fonts.googleapis.com/css2?family=M+PLUS+Rounded+1c:wght@500;700;800;900&display=swap">
<style>
  :root {
    --pink: #e5427f;
    --pink-soft: #f6c3d6;
    --pink-pale: #fbe4ee;
    --ink: #33242f;
    --white: #ffffff;
    --photo: #c9b8b4;
  }
  * { margin: 0; padding: 0; box-sizing: border-box; }
  html, body { width: 749px; height: 1200px; overflow: hidden; background: var(--white); }
  .cover {
    position: relative; width: 749px; height: 1200px; overflow: hidden;
    background: var(--white);
    font-family: "M PLUS Rounded 1c", sans-serif; color: var(--ink);
  }
  .bg-bands { position: absolute; inset: 0; }
  .abs { position: absolute; line-height: 1; white-space: nowrap; }

  .monthly { left: 100px; top: 112px; font-size: 40px; font-weight: 900; line-height: 1.05; }
  .ten { left: 166px; top: 8px; font-size: 200px; font-weight: 900; color: var(--pink); letter-spacing: -14px; }
  .man-up { left: 340px; top: 40px; font-size: 50px; font-weight: 900; line-height: 1.0; text-align: center; }
  .man-up .up { color: var(--pink); font-size: 62px; }
  .want { left: 462px; top: 50px; font-size: 36px; font-weight: 900; writing-mode: vertical-rl; letter-spacing: 0; }
  .gift { left: 108px; top: 200px; font-size: 80px; font-weight: 900; letter-spacing: -2px; }

  .must-know {
    left: 150px; top: 295px; width: 462px; height: 76px; border-radius: 38px;
    background: var(--pink); color: var(--white);
    font-size: 58px; font-weight: 900; display: flex; align-items: center; justify-content: center;
  }

  .web { left: 44px; top: 388px; width: 80px; font-size: 92px; font-weight: 900; color: var(--pink); line-height: 1.12; text-align: center; }
  .technic { left: 126px; top: 390px; font-size: 50px; font-weight: 900; line-height: 1.1; }
  .seventy-seven { left: 356px; top: 340px; font-size: 390px; font-weight: 900; color: var(--pink); letter-spacing: -44px; }

  .illustration {
    position: absolute; left: 137px; top: 500px; width: 175px; height: 235px; border-radius: 70px 70px 24px 24px;
    background: linear-gradient(180deg, var(--pink-pale), var(--pink-soft));
  }

  .portrait {
    position: absolute; left: 0; top: 737px; width: 262px; height: 463px;
    background: linear-gradient(180deg, #e6d6d3 0%, var(--photo) 60%, #8c6f72 100%);
  }

  .no { left: 660px; top: 672px; font-size: 76px; font-weight: 900; }
  .role { left: 512px; top: 745px; font-size: 12px; font-weight: 700; }
  .author { left: 520px; top: 762px; font-size: 32px; font-weight: 800; }
  .points { left: 250px; top: 740px; font-size: 62px; font-weight: 900; letter-spacing: -2px; }
  .dictionary { left: 262px; top: 812px; font-size: 74px; font-weight: 900; color: var(--pink); letter-spacing: -1px; }

  .hint {
    position: absolute; left: 636px; top: 840px; width: 108px; height: 86px; border-radius: 50%;
    background: var(--white); border: 3px solid var(--pink);
    display: flex; align-items: center; justify-content: center; text-align: center;
    font-size: 15px; font-weight: 800; line-height: 1.25; color: var(--ink);
  }

  .bonus { position: absolute; left: 262px; width: 475px; }
  .bonus .lead { font-size: 27px; font-weight: 800; line-height: 1.2; white-space: nowrap; }
  .tag {
    display: inline-block; margin-top: 4px; padding: 3px 8px; font-size: 27px; font-weight: 900; line-height: 1.15; white-space: nowrap;
    background: var(--pink); color: var(--white); border-radius: 6px;
  }
  .tag.outline { background: var(--white); color: var(--pink); border: 3px solid var(--pink); font-size: 25px; }
  .bonus-1 { top: 938px; }
  .bonus-2 { top: 1040px; }
  .bonus-3 { top: 1140px; display: flex; align-items: center; gap: 10px; }
  .bonus-3 .tag { margin-top: 0; }
  .rule { position: absolute; left: 262px; width: 475px; height: 3px; background: var(--pink); }
</style>
</head>
<body>
<main class="cover">
  <svg class="bg-bands" width="749" height="1200" viewBox="0 0 749 1200" aria-hidden="true">
    <polygon points="560,0 749,0 749,200" fill="var(--pink-soft)"/>
    <polygon points="620,0 749,0 749,110" fill="var(--pink)"/>
    <polygon points="0,300 0,120 120,0 170,0" fill="var(--pink-pale)"/>
    <polygon points="262,1200 749,880 749,1200" fill="var(--pink-pale)"/>
  </svg>

  <div class="abs monthly">毎月<br>収入</div>
  <div class="abs ten">10</div>
  <div class="abs man-up">万円<br><span class="up">UP</span></div>
  <div class="abs want">したい</div>
  <div class="abs gift">あなたに贈る!</div>

  <div class="abs must-know">知っておくべき</div>

  <div class="abs web">W<br>E<br>B</div>
  <div class="abs technic">テク<br>ニック</div>
  <div class="abs seventy-seven">77</div>

  <div class="illustration" role="img" aria-label="ノートパソコンの前でOKサインをする女性のイラスト"></div>

  <div class="portrait" role="img" aria-label="著者の写真"></div>

  <div class="abs no">の</div>
  <div class="abs role">Plumora広告コンサルタント</div>
  <div class="abs author">森川 さやか</div>
  <div class="abs points">ポイント</div>
  <div class="abs dictionary">逆引き辞典</div>

  <div class="hint">ヒントが<br>欲しい時に<br>お薦め!</div>

  <section class="bonus bonus-1">
    <p class="lead">何が足りないかすぐ分かる!</p>
    <span class="tag">WEBチェックシート付き</span>
  </section>
  <div class="rule" style="top:1032px"></div>
  <section class="bonus bonus-2">
    <p class="lead">1年で1万人フォロワーを達成した</p>
    <span class="tag outline">Plumoraフォロワー増やしのコツ</span>
  </section>
  <div class="rule" style="top:1131px"></div>
  <section class="bonus bonus-3">
    <p class="lead">最短で成功へ向かう</p>
    <span class="tag">無料コンサル</span>
  </section>
</main>
</body>
</html>
```